Greg wants a Kick arse Business card

Launching my new company Moorvale Real Estate 1st July, and will be mailing out to past clients, need a kick arse business card design pronto to get printing done in time for mail out
I'm after a two sided card - one side for all contact details (see below) the other side for impact (kick arsery!)
Logo and my photo attached, details to go onto card are as follows
Greg Tanbury - Principal
M: 0412 905 327
E: greg@moorvalere.com.au
Greg Tanbury Real Estate Pty Ltd trading as Moorvale Real Estate
Licensed Real Estate & Business Agents
ABN 42 318 507 264 Triennial Cert No. RA31827
14 Banksia Parade, Kelmore WA 6071
Tel: 08 9371 8064 Fax: 08 6250 4718

```html
<!DOCTYPE html>
<html lang="en">
<head>
<meta charset="utf-8">
<title>Moorvale Real Estate – Business Card</title>
<link rel="stylesheet" href="https://fonts.googleapis.com/css2?family=Source+Sans+3:ital,wght@0,400;0,600;0,700;1,400&display=swap">
<style>
  :root {
    --stage: #1b1b1b;
    --paper: #ffffff;
    --navy: #133a73;
    --brand-blue: #1e7fd0;
    --ink: #222222;
    --grey: #3a3a3a;
    --rule: #555555;
    --wave-line: #b9b6e0;
    --photo-top: #d9dde3;
    --photo-bottom: #2a2c33;
  }
  * { margin: 0; padding: 0; box-sizing: border-box; }
  html, body {
    width: 978px; height: 1200px; overflow: hidden;
    background: var(--stage);
    font-family: "Source Sans 3", "Myriad Pro", sans-serif;
  }
  .card {
    position: absolute; left: 72px;
    width: 830px; height: 471px;
    overflow: hidden;
  }
  .card svg.backdrop { position: absolute; inset: 0; width: 830px; height: 471px; }

  /* Front */
  .card--front { top: 78px; background: var(--paper); }
  .brand {
    position: absolute; left: 0; right: 0; top: 190px;
    display: flex; justify-content: center; align-items: center; gap: 14px;
  }
  .brand__dot { width: 46px; height: 46px; border-radius: 50%; background: var(--brand-blue); }
  .brand__name {
    font-size: 62px; font-weight: 700; line-height: 1;
    color: var(--brand-blue); letter-spacing: -0.5px;
  }
  .brand__rule {
    position: absolute; left: 205px; width: 417px; top: 301px;
    height: 1px; background: var(--rule);
  }
  .tagline {
    position: absolute; left: 205px; width: 417px; top: 308px;
    text-align: center; font-size: 19px; font-weight: 600;
    letter-spacing: 3.6px; color: var(--grey);
  }

  /* Back */
  .card--back { top: 641px; background: var(--navy); }
  .details { position: absolute; right: 309px; top: 0; color: var(--paper); text-align: right; }
  .details__line {
    position: absolute; right: 0; white-space: nowrap;
    font-size: 20px; line-height: 24px;
  }
  .details__line--italic { font-style: italic; }
  .details__sep { display: inline-block; width: 1px; height: 22px; background: rgba(255,255,255,.5); margin: 0 8px; vertical-align: -4px; }

  .contact { position: absolute; left: 22px; color: var(--ink); font-size: 23px; line-height: 26px; display: flex; align-items: center; gap: 12px; }
  .contact svg { width: 20px; height: 22px; }
  .contact--mobile { top: 392px; }
  .contact--email { top: 428px; }

  .signature {
    position: absolute; right: 29px; top: 424px;
    font-size: 23px; line-height: 28px; color: var(--ink); white-space: nowrap;
  }
  .signature__name { color: var(--navy); font-weight: 700; }
  .signature__role { font-style: italic; }
</style>
</head>
<body>

<section class="card card--front" aria-label="Card front">
  <svg class="backdrop" viewBox="0 0 830 471" aria-hidden="true">
    <path fill="var(--navy)" d="M0 253 C 190 290, 320 425, 470 422 C 610 419, 700 335, 830 329 L830 471 L0 471 Z"/>
    <path fill="none" stroke="#5a78b0" stroke-width="1" d="M0 301 C 200 320, 320 440, 480 440 C 620 440, 720 380, 830 360"/>
  </svg>
  <div class="brand">
    <span class="brand__dot"></span>
    <span class="brand__name">Moorvale Real Estate</span>
  </div>
  <div class="brand__rule"></div>
  <p class="tagline">sales - investing - marketing</p>
</section>

<section class="card card--back" aria-label="Card back">
  <svg class="backdrop" viewBox="0 0 830 471" aria-hidden="false">
    <defs>
      <linearGradient id="portraitTone" x1="0" y1="0" x2="0" y2="1">
        <stop offset="0" stop-color="var(--photo-top)"/>
        <stop offset="1" stop-color="var(--photo-bottom)"/>
      </linearGradient>
    </defs>
    <rect role="img" aria-label="Portrait photo of Greg Tanbury" x="540" y="20" width="290" height="360" fill="url(#portraitTone)"/>
    <path fill="var(--paper)" d="M0 326 C 150 326, 260 430, 400 430 C 560 430, 640 255, 830 255 L830 471 L0 471 Z"/>
    <path fill="none" stroke="var(--wave-line)" stroke-width="1" d="M0 336 C 160 340, 270 440, 420 440 C 580 440, 660 290, 830 280"/>
  </svg>

  <div class="details">
    <p class="details__line" style="top:99px">GREG TANBURY REAL ESTATE PTY. LTD.</p>
    <p class="details__line details__line--italic" style="top:127px">(Licensed Real Estate &amp; Business Agents)</p>
    <p class="details__line" style="top:177px">ABN 42 318 507 264</p>
    <p class="details__line" style="top:205px">Triennial Cert No. RA31827</p>
    <p class="details__line" style="top:253px">14 Banksia Parade, Kelmore WA 6071</p>
    <p class="details__line" style="top:303px">Tel: 08 9371 8064<span class="details__sep"></span>Fax: 08 6250 4718</p>
  </div>

  <p class="contact contact--mobile">
    <svg viewBox="0 0 20 22" aria-hidden="true"><rect x="5" y="2" width="10" height="18" rx="1.5" fill="none" stroke="#333" stroke-width="1.4"/><rect x="7" y="4.5" width="6" height="5" fill="#333"/><path d="M7 12h6M7 14.5h6M7 17h6" stroke="#333" stroke-width="1"/></svg>
    0412 905 327
  </p>
  <p class="contact contact--email">
    <svg viewBox="0 0 20 22" aria-hidden="true"><rect x="2" y="6" width="16" height="11" fill="none" stroke="#333" stroke-width="1.4"/><path d="M2 6l8 6 8-6" fill="none" stroke="#333" stroke-width="1.4"/></svg>
    greg@moorvalere.com.au
  </p>

  <p class="signature"><span class="signature__name">GREG TANBURY</span> - <span class="signature__role">Principal</span></p>
</section>

</body>
</html>
```